1 Home page redesign for existing repair service site.

We need a refresh of our existing website that looks more 2017. We have made a mockup of the content that we want and a sample of where we want it. Nothing is set in stone, if you have better ideas of where things should go, feel free.

You can see our current site at http://www.tokelmo.gr

The colors should stay orange/black/grey.

In many of the "boxes/banners" we will need images. Feel free to find in glade barn as we have an account.

We have made notes throughout the wireframe that we have attached on what we are looking for. Let us know if you have any questions. Thanks.

Target Market(s)

People using technology and breaking it

Industry/Entity Type

It Service

Number of Pages Required

1 page

Font styles to use
Sans Serif

Requirements
Must have
• Must have a modern, professional look and feel. Need custom graphics and icons.

```html
<!DOCTYPE html>
<html lang="en">
<head>
<meta charset="utf-8">
<title>Tokelmo – Phone, Laptop &amp; Tablet Repair</title>
<link href="https://fonts.googleapis.com/css2?family=Barlow:wght@400;500;600;700&family=Open+Sans:wght@400;600;700&display=swap" rel="stylesheet">
<style>
:root{
  --orange:#f7941d;
  --ink:#1f1f1f;
  --dark:#2a2a2a;
  --darker:#1c1c1c;
  --grey:#c9cacc;
  --light:#e8e8ea;
  --paper:#ffffff;
  --muted:#8a8a8a;
  --text:#444;
}
*{box-sizing:border-box;margin:0;padding:0}
html,body{width:1200px;height:3822px;overflow:hidden}
body{font-family:"Open Sans",Arial,sans-serif;color:var(--text);background:var(--paper);font-size:13px}
.wrap{width:980px;margin:0 auto;position:relative;height:100%}
h1,h2,h3,h4,.display{font-family:"Barlow",Arial,sans-serif}
svg{display:block}

/* top bar */
.topbar{height:46px;background:var(--darker);color:#fff;font-size:12px}
.topbar .wrap{display:flex;align-items:center;justify-content:space-between}
.topbar .contact{display:flex;gap:28px;align-items:center}
.topbar .contact span{display:flex;align-items:center;gap:8px}
.dot-ic{width:16px;height:16px;border-radius:50%;background:var(--orange);flex:none}
.topbar .right{display:flex;gap:14px;align-items:center}
.lang b{color:var(--orange);font-weight:600}
.social{display:flex;gap:10px}
.social i{width:12px;height:12px;border-radius:50%;background:#9a9a9a;display:block}

/* nav */
.nav{height:69px;background:var(--light)}
.nav .wrap{display:flex;align-items:center;justify-content:space-between}
.brand{display:flex;align-items:center;gap:10px;font-family:"Barlow",sans-serif;font-weight:700;font-size:30px;color:var(--ink)}
.brand .sq{width:34px;height:34px;background:var(--orange);border-radius:4px}
.menu{display:flex;font-family:"Barlow",sans-serif;font-size:13px;font-weight:600;text-transform:uppercase;color:var(--ink)}
.menu a{padding:0 16px;border-left:1px solid #bbb;line-height:18px}
.menu a:first-child{border-left:0}

/* hero */
.hero{height:489px;position:relative;overflow:hidden;
  background:
    radial-gradient(ellipse 480px 300px at 92% 40%,#5e5e5e 0%,rgba(94,94,94,0) 100%),
    linear-gradient(90deg,#f2f2f2 0%,#d6d6d6 45%,#8d8d8d 80%,#6a6a6a 100%)}
.hero .art{position:absolute;left:0;top:0;width:720px;height:489px;
  background:
    radial-gradient(ellipse 170px 120px at 62% 22%,rgba(60,70,72,.55) 0%,rgba(60,70,72,0) 100%),
    radial-gradient(ellipse 210px 170px at 26% 44%,#2f3a3c 0%,#50605f 45%,rgba(120,130,130,0) 100%),
    radial-gradient(ellipse 320px 70px at 52% 84%,#3e3e40 0%,#6d6d70 55%,rgba(160,160,160,0) 100%),
    linear-gradient(160deg,rgba(0,0,0,0) 10%,rgba(40,45,46,.35) 40%,rgba(0,0,0,0) 70%)}
.hero .tag{position:absolute;right:110px;top:75px;text-align:right;font-family:"Barlow",sans-serif;font-weight:500;font-size:38px;line-height:58px;color:#fff}
.hero .tag span{display:block}
.hero .big{position:absolute;right:110px;top:240px;text-align:right;font-family:"Barlow",sans-serif;font-weight:600;font-size:62px;line-height:76px;letter-spacing:2px;color:#4c4c4c}

/* features */
.features{height:186px;background:var(--paper)}
.features .wrap{display:grid;grid-template-columns:repeat(4,1fr);align-items:center;text-align:center}
.feat svg{margin:0 auto 14px}
.feat h4{font-size:13px;font-weight:600;text-transform:uppercase;color:var(--ink);letter-spacing:.3px}
.feat p{font-size:11px;color:var(--muted);margin-top:4px;text-transform:uppercase}

/* promo */
.promo{height:300px;display:flex}
.promo .half{flex:1;position:relative;color:#fff}
.promo .left{background:
    radial-gradient(ellipse 90px 130px at 14% 40%,#c9c4bc 0%,#7d8a83 45%,rgba(60,60,60,0) 100%),
    radial-gradient(ellipse 200px 160px at 20% 75%,#8a6f5e 0%,#4b3e37 55%,rgba(35,35,35,0) 100%),
    radial-gradient(ellipse 160px 140px at 70% 90%,#6a5547 0%,rgba(35,35,35,0) 100%),
    linear-gradient(120deg,#3a3a3a,#1f1f1f 55%,#2c2c2c)}
.promo .right{background:
    radial-gradient(ellipse 220px 150px at 78% 55%,#5a5a5a 0%,#2f2f2f 60%,rgba(40,40,40,0) 100%),
    radial-gradient(ellipse 120px 90px at 92% 20%,#6d6d6d 0%,rgba(60,60,60,0) 100%),
    linear-gradient(120deg,#3c3c3c,#262626 55%,#353535)}
.promo h3{position:absolute;font-size:28px;font-weight:600;text-transform:uppercase}
.promo h3 b{color:var(--orange);font-weight:600}
.promo p{position:absolute;font-size:13px;text-transform:uppercase;line-height:22px}
.btn-dark{display:inline-block;background:#222;color:#fff;font-family:"Barlow",sans-serif;font-weight:600;font-size:12px;text-transform:uppercase;padding:16px 22px}
.promo .note{font-size:10px!important}

/* cards */
.cards-band{height:388px;background:var(--grey)}
.cards{display:flex;gap:26px;padding-top:59px}
.card{width:224px;height:268px;position:relative;color:#fff;overflow:hidden}
.card.c1{background:
    radial-gradient(ellipse 90px 80px at 70% 18%,#8b8f99 0%,rgba(90,95,105,0) 100%),
    radial-gradient(ellipse 150px 90px at 50% 85%,#6e6a66 0%,rgba(60,60,60,0) 100%),
    linear-gradient(160deg,#5d636b,#33363a 55%,#2a2a2a)}
.card.c2{background:
    radial-gradient(ellipse 110px 80px at 55% 22%,#5e5e5e 0%,rgba(60,60,60,0) 100%),
    radial-gradient(ellipse 120px 70px at 40% 90%,#444 0%,rgba(30,30,30,0) 100%),
    linear-gradient(160deg,#2e2e2e,#121212)}
.card.c3{background:
    radial-gradient(ellipse 100px 90px at 50% 35%,#262626 0%,rgba(40,40,40,0) 100%),
    radial-gradient(ellipse 80px 60px at 30% 80%,#7a7a7a 0%,rgba(90,90,90,0) 100%),
    linear-gradient(160deg,#8b8b8b,#555 55%,#333)}
.card.c4{background:
    radial-gradient(ellipse 80px 110px at 55% 30%,#6f8f6a 0%,#3e5a40 45%,rgba(40,55,42,0) 100%),
    linear-gradient(160deg,#39413b,#1b1e1c)}
.card .body{position:absolute;left:14px;right:14px;top:108px}
.card.mid .body{top:92px;text-align:center}
.card h4{font-size:16px;font-weight:700;text-transform:uppercase;line-height:19px}
.card p{font-size:10px;line-height:14px;margin-top:10px}
.card .btn-dark{margin-top:16px;padding:10px 14px;font-size:10px}

/* repair list */
.repair{height:522px;background:#f1f1f2;padding-top:55px}
.sec-title{font-size:23px;font-weight:600;text-transform:uppercase;color:var(--ink)}
.sec-title::after{content:"";display:block;width:42px;height:2px;background:var(--ink);margin-top:8px}
.repair .sub{font-size:11px;font-weight:700;text-transform:uppercase;color:var(--ink);margin-top:10px}
.repair .intro{font-size:11px;line-height:20px;text-transform:uppercase;margin-top:12px;width:860px;color:#333}
.devices{display:grid;grid-template-columns:repeat(5,1fr);row-gap:50px;margin-top:48px}
.dev{text-align:center;font-size:11px;color:var(--ink)}
.dev svg{margin:0 auto 14px;height:62px}

/* repair option */
.option{height:275px;color:#fff;text-align:center;padding-top:50px;
  background:
    radial-gradient(ellipse 260px 160px at 50% 55%,#4a3a30 0%,#2a2420 50%,rgba(20,20,20,0) 100%),
    radial-gradient(ellipse 120px 80px at 46% 70%,rgba(200,80,40,.35) 0%,rgba(0,0,0,0) 100%),
    linear-gradient(90deg,#0f0f0f,#222 50%,#0f0f0f)}
.center-title{font-size:23px;font-weight:600;text-transform:uppercase;display:inline-block}
.center-title::after{content:"";display:block;width:42px;height:2px;background:currentColor;margin:8px auto 0}
.opts{display:grid;grid-template-columns:repeat(4,1fr);margin-top:48px;font-size:13px}
.opts svg{margin:0 auto 12px}

/* why */
.why{height:459px;background:var(--grey);text-align:center;padding-top:48px;position:relative}
.why .center-title{color:var(--ink)}
.why .cards{padding-top:62px;text-align:left}
.arrow{position:absolute;top:245px}

/* testimonials */
.testi{height:497px;color:#fff;text-align:center;padding-top:50px;
  background:
    radial-gradient(ellipse 260px 260px at 88% 55%,#7a4a2a 0%,#4a3428 45%,rgba(50,45,42,0) 100%),
    radial-gradient(ellipse 300px 200px at 40% 60%,#3d3d3d 0%,rgba(45,45,45,0) 100%),
    linear-gradient(90deg,#262626,#333 55%,#2b2b2b)}
.stars{display:flex;justify-content:center;gap:3px;margin-top:10px}
.tcards{display:flex;gap:45px;margin-top:30px;text-align:left}
.tcard{width:297px;height:320px;background:rgba(30,30,30,.45);border-top:3px solid rgba(255,255,255,.4)}
.tcard .head{background:#fff;color:var(--ink);padding:12px 18px 12px}
.tcard h4{font-size:14px;font-weight:600}
.tcard li{list-style:none;font-size:10px;margin-top:6px;display:flex;gap:8px;align-items:center}
.tcard li::before{content:"";width:8px;height:8px;background:var(--ink);display:block}
.quote{margin:22px 20px 0;background:#e9e9e9;color:#333;font-size:10px;line-height:15px;padding:14px 14px;position:relative}
.quote::after{content:"";position:absolute;right:28px;bottom:-10px;border:10px solid transparent;border-top-color:#e9e9e9;border-bottom:0}
.who{text-align:right;font-size:10px;margin:18px 22px 0}

/* subscribe */
.subscribe{height:148px;background:var(--grey)}
.subscribe .wrap{display:flex;justify-content:space-between;align-items:center}
.subscribe h3{font-size:24px;font-weight:600;color:var(--ink)}
.subscribe p{font-size:11px;color:var(--ink);margin-top:6px}
.form{display:flex}
.form span{width:368px;height:44px;background:#111;color:#fff;font-size:12px;padding:14px 16px}
.form b{width:112px;height:44px;background:var(--orange);color:#fff;font-size:12px;font-weight:600;text-align:center;line-height:44px}

/* footer */
.footer{height:392px;background:var(--dark);color:#ddd;padding-top:38px}
.footer .cols{display:grid;grid-template-columns:330px 335px 1fr}
.footer h5{font-family:"Barlow",sans-serif;font-size:15px;font-weight:600;color:#fff;margin-bottom:14px}
.links li{list-style:none;font-size:11px;line-height:27px}
.social-row{display:flex;align-items:center;gap:14px;margin-top:28px;font-size:12px;font-weight:600;color:#fff}
.blog li{list-style:none;background:#3a3a3a;width:295px;padding:12px 14px;margin-bottom:4px;font-size:10px;line-height:16px}
.blog li b{display:block;border-bottom:1px solid #555;padding-bottom:4px;margin-bottom:6px;font-weight:400;color:#fff}
.ci{display:flex;gap:12px;margin-bottom:18px}
.ci h6{font-size:11px;font-weight:600;text-transform:uppercase;color:#fff}
.ci p{font-size:11px;line-height:17px}
.ci a{color:var(--orange);font-size:11px}

.bottom{height:51px;background:#fff}
.bottom .wrap{display:flex;justify-content:space-between;align-items:center;font-size:11px}
.cardsp{display:flex;gap:6px}
.cardsp i{width:30px;height:19px;background:#d4d6da;border-radius:2px;display:block}
</style>
</head>
<body>

<header class="topbar">
  <div class="wrap">
    <div class="contact">
      <span><i class="dot-ic"></i>210 555 0142</span>
      <span><i class="dot-ic"></i>Live Chat</span>
    </div>
    <div class="right">
      <span class="lang">GER | <b>ENG</b></span>
      <div class="social"><i></i><i></i><i></i><i></i><i></i><i></i></div>
    </div>
  </div>
</header>

<nav class="nav">
  <div class="wrap">
    <div class="brand"><span class="sq"></span>Tokelmo</div>
    <div class="menu">
      <a>Repair ▾</a><a>Services ▾</a><a>20 Stores</a><a>Blog</a><a>Quick Links ▾</a>
    </div>
  </div>
</nav>

<section class="hero">
  <div class="art" role="img" aria-label="Laptop with its screen shattering into flying glass pieces"></div>
  <div class="tag"><span>We fix broken Phones</span><span>Laptops &amp; Tablets</span></div>
  <div class="big"><div>REPAIR YOUR</div><div>GADGETS</div></div>
</section>

<section class="features">
  <div class="wrap">
    <div class="feat">
      <svg width="40" height="40" viewBox="0 0 40 40"><circle cx="20" cy="20" r="17" fill="none" stroke="#f7941d" stroke-width="3"/><circle cx="14" cy="16" r="2.5" fill="#f7941d"/><circle cx="26" cy="16" r="2.5" fill="#f7941d"/><path d="M12 24q8 8 16 0" fill="none" stroke="#f7941d" stroke-width="3"/></svg>
      <h4>35000 Happy Clients</h4><p>Yep, we fix a lot of devices !</p>
    </div>
    <div class="feat">
      <svg width="48" height="40" viewBox="0 0 48 40"><rect x="2" y="8" width="28" height="22" fill="#f7941d"/><path d="M30 14h9l7 8v8H30z" fill="#f7941d"/><circle cx="11" cy="32" r="4" fill="#fff" stroke="#f7941d" stroke-width="3"/><circle cx="37" cy="32" r="4" fill="#fff" stroke="#f7941d" stroke-width="3"/></svg>
      <h4>Free Shipping</h4><p>With next day courier*</p>
    </div>
    <div class="feat">
      <svg width="40" height="40" viewBox="0 0 40 40"><circle cx="16" cy="7" r="5" fill="#f7941d"/><path d="M10 14h10l4 10-5 2-2-5v17h-5V24l-3 4-4-2z" fill="#f7941d"/><rect x="25" y="14" width="12" height="12" fill="#f7941d"/></svg>
      <h4>Free Home Pickup</h4><p>And delivery in Athens</p>
    </div>
    <div class="feat">
      <svg width="44" height="40" viewBox="0 0 44 40"><ellipse cx="21" cy="22" rx="16" ry="12" fill="#f7941d"/><rect x="10" y="30" width="5" height="8" fill="#f7941d"/><rect x="26" y="30" width="5" height="8" fill="#f7941d"/><rect x="17" y="4" width="8" height="8" rx="4" fill="#f7941d"/><path d="M36 20l6-2v6l-6-1z" fill="#f7941d"/></svg>
      <h4>Save 50% - 75%</h4><p>On multiple repairs to your</p>
    </div>
  </div>
</section>

<section class="promo">
  <div class="half left" role="img" aria-label="Hand holding a smartphone showing a store map">
    <h3 style="left:250px;top:30px"><b style="color:#fff">20</b> <b>TOKELMO</b> LOCATION</h3>
    <p style="left:322px;top:85px">Find a store near you</p>
    <span class="btn-dark" style="position:absolute;left:445px;top:200px">View more</span>
  </div>
  <div class="half right" role="img" aria-label="Opened smartphone during screen repair">
    <h3 style="left:40px;top:30px">Low Price Guarantee</h3>
    <p style="left:40px;top:85px;width:420px">Find a lower price for your phone or tablet repair ?<br>We will match it!*</p>
    <p class="note" style="left:175px;top:236px">*Term and conditions apply. Click to read more</p>
  </div>
</section>

<section class="cards-band">
  <div class="wrap">
    <div class="cards">
      <div class="card c1" role="img" aria-label="Technician repairing a laptop at an open service desk">
        <div class="body"><h4>Open Service Area</h4><p>repairs right in front of you no closed doors/no back room</p><span class="btn-dark">View more</span></div>
      </div>
      <div class="card c2 mid" role="img" aria-label="Repair tools on a dark workbench">
        <div class="body"><h4>Save 50-75% on multiple repairs</h4><p>If your device need more than 1 part replaced,save upto 75% on addition parts.</p></div>
      </div>
      <div class="card c3 mid" role="img" aria-label="Laptop bag and accessories">
        <div class="body" style="top:112px"><h4>Accessories</h4></div>
      </div>
      <div class="card c4 mid" role="img" aria-label="Smartphone showing a repair checklist">
        <div class="body" style="top:100px"><h4>20 Minute Repairs</h4><p>most repairs can be completed in about 20 minutes.</p></div>
      </div>
    </div>
  </div>
</section>

<section class="repair">
  <div class="wrap">
    <h2 class="sec-title">What We Repair</h2>
    <div class="sub">See our services and pricing</div>
    <p class="intro">We offer first class customer service with fast, reliable and affordable repairs. Whether you visit any of our stores or send us your device, you can expect to have the same amazing customer experience.</p>
    <div class="devices">
      <div class="dev"><svg width="30" height="62" viewBox="0 0 30 62"><rect x="2" y="2" width="26" height="56" rx="5" fill="#1f1f1f"/><rect x="5" y="10" width="20" height="38" fill="#fff"/><circle cx="15" cy="53" r="2.5" fill="#fff"/></svg>Phonix Repair</div>
      <div class="dev"><svg width="44" height="62" viewBox="0 0 44 62"><rect x="2" y="2" width="40" height="56" rx="4" fill="#1f1f1f"/><rect x="6" y="8" width="32" height="42" fill="#fff"/><circle cx="22" cy="54" r="2" fill="#fff"/></svg>Tablix Repair</div>
      <div class="dev"><svg width="26" height="62" viewBox="0 0 26 62"><rect x="2" y="2" width="22" height="56" rx="4" fill="#1f1f1f"/><rect x="5" y="9" width="16" height="38" fill="#fff"/><circle cx="13" cy="52" r="2" fill="#fff"/></svg>Podix Touch Repair</div>
      <div class="dev"><svg width="30" height="62" viewBox="0 0 30 62"><rect x="3" y="2" width="24" height="56" rx="7" fill="none" stroke="#1f1f1f" stroke-width="3"/><rect x="7" y="10" width="16" height="38" fill="#1f1f1f"/></svg>Samvel Repair</div>
      <div class="dev"><svg width="34" height="62" viewBox="0 0 34 62"><rect x="2" y="2" width="30" height="56" rx="5" fill="#1f1f1f"/><rect x="6" y="8" width="22" height="18" fill="#fff"/><g fill="#fff"><rect x="6" y="32" width="5" height="4"/><rect x="14" y="32" width="5" height="4"/><rect x="22" y="32" width="5" height="4"/><rect x="6" y="40" width="5" height="4"/><rect x="14" y="40" width="5" height="4"/><rect x="22" y="40" width="5" height="4"/><rect x="6" y="48" width="5" height="4"/><rect x="14" y="48" width="5" height="4"/><rect x="22" y="48" width="5" height="4"/></g></svg>Berrymax Repair</div>
      <div class="dev"><svg width="66" height="62" viewBox="0 0 66 62"><rect x="2" y="4" width="62" height="40" rx="2" fill="#1f1f1f"/><rect x="6" y="8" width="54" height="30" fill="#fff"/><path d="M26 44h14l3 12H23z" fill="#1f1f1f"/><rect x="18" y="56" width="30" height="3" fill="#1f1f1f"/></svg>Desko Repairs</div>
      <div class="dev"><svg width="70" height="62" viewBox="0 0 70 62"><rect x="10" y="10" width="50" height="34" rx="2" fill="none" stroke="#1f1f1f" stroke-width="3"/><path d="M2 48h66l-4 6H6z" fill="#1f1f1f"/></svg>Notebo Repair</div>
      <div class="dev"><svg width="60" height="62" viewBox="0 0 60 62"><rect x="2" y="6" width="38" height="30" fill="none" stroke="#1f1f1f" stroke-width="3"/><rect x="16" y="36" width="10" height="8" fill="#1f1f1f"/><rect x="10" y="44" width="22" height="3" fill="#1f1f1f"/><rect x="44" y="6" width="14" height="48" fill="#1f1f1f"/><rect x="47" y="12" width="8" height="2" fill="#fff"/><rect x="47" y="17" width="8" height="2" fill="#fff"/></svg>Computer Repair</div>
      <div class="dev"><svg width="70" height="62" viewBox="0 0 70 62"><rect x="10" y="10" width="50" height="34" rx="2" fill="#1f1f1f"/><rect x="14" y="14" width="42" height="26" fill="#fff"/><path d="M2 48h66l-4 6H6z" fill="#1f1f1f"/></svg>Laptop Repair</div>
      <div class="dev"><svg width="50" height="62" viewBox="0 0 50 62"><circle cx="25" cy="26" r="12" fill="#1f1f1f"/><rect x="20" y="38" width="10" height="10" fill="#1f1f1f"/><g stroke="#1f1f1f" stroke-width="3"><path d="M25 4v6M6 26h6M38 26h6M11 12l4 4M39 12l-4 4"/></g><path d="M20 26l4 4 6-8" fill="none" stroke="#fff" stroke-width="2.5"/></svg>Business Services</div>
    </div>
  </div>
</section>

<section class="option" role="img" aria-label="Dark background photo of a repair workshop">
  <div class="wrap">
    <h2 class="center-title">Repair Option</h2>
    <div class="opts">
      <div><svg width="30" height="40" viewBox="0 0 30 40"><path d="M15 2a13 13 0 0 1 13 13c0 10-13 23-13 23S2 25 2 15A13 13 0 0 1 15 2z" fill="#f7941d"/><circle cx="15" cy="15" r="5" fill="#1a1a1a"/></svg>find a store near you ?</div>
      <div><svg width="44" height="40" viewBox="0 0 44 40"><path d="M10 4h24v20H10z" fill="none" stroke="#f7941d" stroke-width="3"/><path d="M2 30h14l6 4h12l8-6v8H2z" fill="#f7941d"/></svg>Send us your device</div>
      <div><svg width="48" height="40" viewBox="0 0 48 40"><rect x="2" y="8" width="28" height="22" fill="#f7941d"/><path d="M30 14h9l7 8v8H30z" fill="#f7941d"/><circle cx="11" cy="32" r="4" fill="#1a1a1a" stroke="#f7941d" stroke-width="3"/><circle cx="37" cy="32" r="4" fill="#1a1a1a" stroke="#f7941d" stroke-width="3"/></svg>Fee pickup athens</div>
      <div><svg width="40" height="40" viewBox="0 0 40 40"><circle cx="20" cy="20" r="17" fill="none" stroke="#f7941d" stroke-width="3"/><text x="20" y="25" text-anchor="middle" font-family="Barlow,sans-serif" font-weight="700" font-size="13" fill="#f7941d">24/7</text></svg>24x7 customer service</div>
    </div>
  </div>
</section>

<section class="why">
  <div class="wrap">
    <h2 class="center-title">Why Choose Tokelmo</h2>
    <svg class="arrow" style="left:-28px" width="14" height="24" viewBox="0 0 14 24"><path d="M12 2L3 12l9 10" fill="none" stroke="#111" stroke-width="3"/></svg>
    <svg class="arrow" style="right:-28px" width="14" height="24" viewBox="0 0 14 24"><path d="M2 2l9 10-9 10" fill="none" stroke="#111" stroke-width="3"/></svg>
    <div class="cards">
      <div class="card c1" role="img" aria-label="Technician repairing a laptop at an open service desk">
        <div class="body"><h4>Open Service Area</h4><p>repairs right in front of you no closed doors/no back room</p><span class="btn-dark">View more</span></div>
      </div>
      <div class="card c2 mid" role="img" aria-label="Repair tools on a dark workbench">
        <div class="body"><h4>Save 50-75% on multiple repairs</h4><p>If your device need more than 1 part replaced,save upto 75% on addition parts.</p></div>
      </div>
      <div class="card c3 mid" role="img" aria-label="Laptop bag and accessories">
        <div class="body" style="top:112px"><h4>Accessories</h4></div>
      </div>
      <div class="card c4 mid" role="img" aria-label="Smartphone showing a repair checklist">
        <div class="body" style="top:100px"><h4>20 Minute Repairs</h4><p>most repairs can be completed in about 20 minutes.</p></div>
      </div>
    </div>
  </div>
</section>

<section class="testi" role="img" aria-label="Dim background photo of hands holding a smartphone">
  <div class="wrap">
    <h2 class="display" style="font-size:23px;font-weight:600;text-transform:uppercase">What Our Customer Says</h2>
    <div class="stars">
      <svg width="80" height="14" viewBox="0 0 80 14"><g fill="#f7941d"><path id="st" d="M7 0l2 5h5l-4 3 2 5-5-3-5 3 2-5-4-3h5z"/><use href="#st" x="16"/><use href="#st" x="32"/><use href="#st" x="48"/><use href="#st" x="64"/></g></svg>
    </div>
    <div class="tcards">
      <div class="tcard">
        <div class="head"><h4>laptop repair</h4><ul><li>overheating</li></ul></div>
        <div class="quote">For months my laptop was in meltdown mode. It was terribly slow and I was getting error messages and frequent shutdowns. Since my whole life is on it I was desperate for a better solution because I didn't want to say goodbye to my laptop or my files. The team saved all my precious files and now my computer is really fast! I recommend them without any hesitation. You guys are fantastic!</div>
        <div class="who">Eleni R., Marousi</div>
      </div>
      <div class="tcard">
        <div class="head"><h4>Phonix 5 Repair</h4><ul><li>Water Damage Repair</li><li>Dock Connector Replacement</li></ul></div>
        <div class="quote">My phone took a dive in the deep end of the pool and I never crossed my mind that it could be saved! Congratulations, you fixed it!</div>
        <div class="who">Stavros K., Patra</div>
      </div>
      <div class="tcard">
        <div class="head"><h4>Phonix 6 Repair</h4><ul><li>Screen Replacement</li></ul></div>
        <div class="quote">I just can't part with my phone, I can't do anything without it! When my screen broke I went to the shop feeling helpless. They replaced the screen incredibly fast in only 15 minutes!!! I was relieved, excited and grateful! Thank you is not enough!</div>
        <div class="who">Dora L., Kifisia</div>
      </div>
    </div>
  </div>
</section>

<section class="subscribe">
  <div class="wrap">
    <div><h3>SUBSCRIBE</h3><p>* Subscribe to the Tokelmo newsletter</p></div>
    <div class="form"><span>email address</span><b>subscribe</b></div>
  </div>
</section>

<footer class="footer">
  <div class="wrap">
    <div class="cols">
      <div>
        <h5>quick links</h5>
        <ul class="links"><li>About Tokelmo</li><li>Business Services</li><li>Schedule a Pickup</li><li>Job openings</li><li>Shipping Instructions</li><li>Privacy policy</li><li>Send your device with ParcelNook</li></ul>
        <div class="social-row">social links : <div class="social"><i></i><i></i><i></i><i></i><i></i><i></i></div></div>
      </div>
      <div>
        <h5>tokelmo blog</h5>
        <ul class="blog">
          <li><b>26.11.2016</b>These are the 3 simple but important steps to look after our PC, but most people neglect</li>
          <li><b>26.11.2016</b>These are the 3 simple but important steps to look after our PC, but most people neglect</li>
          <li><b>26.11.2016</b>These are the 3 simple but important steps to look after our PC, but most people neglect</li>
        </ul>
      </div>
      <div>
        <h5>contact info</h5>
        <div class="ci"><i class="dot-ic"></i><div><h6>Contact our call center</h6><p>Call to speak to a customer service rep.</p><a>210 555 0142</a></div></div>
        <div class="ci"><i class="dot-ic"></i><div><h6>Email support</h6><p>We usually respond within 24 hours</p><a>Click to send email</a></div></div>
        <div class="ci"><i class="dot-ic"></i><div><h6>Live chat</h6><p>Chat with an Tokelmo technician now</p><a>Click to chat</a></div></div>
      </div>
    </div>
  </div>
</footer>

<div class="bottom">
  <div class="wrap">
    <span>© Tokelmo 2014</span>
    <div class="cardsp"><i></i><i></i><i></i><i></i><i></i></div>
  </div>
</div>

</body>
</html>
```